Design for homepage Greek Traditional Tavern

Need design for an Greek Traditional Tavern with subpages so should be links also like: Contact us, photos, menu, find us etc etc
The design is for index page and want the feeling should be same as when you visit an old greek tavern
If any questions just write

```html
<!DOCTYPE html>
<html lang="en">
<head>
<meta charset="utf-8">
<title>Kefalos Tavern</title>
<link rel="stylesheet" href="https://fonts.googleapis.com/css2?family=Questrial&family=Open+Sans:wght@400;700&display=swap">
<style>
:root{
  --accent:#e2652c;
  --bg-dark:#3a291f;
  --bg-top:#3d2b21;
  --band:#5a4233;
  --band-line:#4e392c;
  --topbar:#2e2019;
  --text-light:#ffffff;
  --text-muted:#8e7563;
  --topbar-text:#b9a697;
  --rule:#6e5a4c;
  --dot:#2c1f18;
  --hero-light:#f3f2ef;
  --hero-mid:#e4e2dc;
}
*{margin:0;padding:0;box-sizing:border-box}
html,body{width:1200px;height:774px;overflow:hidden}
body{position:relative;background:var(--bg-dark);font-family:"Questrial",sans-serif;color:var(--text-light)}
.page-top{position:absolute;left:0;top:0;width:1200px;height:393px;background:var(--bg-top)}
.accent-line{position:absolute;left:0;top:0;width:1200px;height:5px;background:var(--accent)}
.info-bar{position:absolute;left:0;top:5px;width:1200px;height:22px;background:var(--topbar);display:flex;justify-content:center;align-items:center;gap:26px;font-family:"Open Sans",sans-serif;font-size:10px;color:var(--topbar-text);letter-spacing:.2px}
.info-bar span{display:flex;align-items:center;gap:6px}
.band{position:absolute;left:0;top:393px;width:1200px;height:252px;background:var(--band);border-top:1px solid var(--band-line);border-bottom:1px solid #2f2119}
.site-name{position:absolute;left:0;top:50px;width:1200px;text-align:center;font-size:45px;color:var(--accent);font-weight:400;letter-spacing:.5px}
.main-nav{position:absolute;left:155px;top:128px;width:891px;height:24px;display:flex;align-items:center}
.main-nav .rule{flex:1;height:4px;background:var(--rule);border-radius:1px}
.main-nav ul{list-style:none;display:flex;gap:27px;padding:0 20px;font-family:"Open Sans",sans-serif;font-weight:700;font-size:14px;text-transform:uppercase}
.main-nav a{color:var(--text-light);text-decoration:none}
.slider{position:absolute;left:156px;top:168px;width:892px;height:290px;border:3px solid #f3f1ee;border-radius:3px;box-shadow:0 2px 8px rgba(0,0,0,.45);overflow:hidden}
.slide-photo{width:100%;height:100%;background:radial-gradient(ellipse at 50% 50%,var(--hero-light) 0%,var(--hero-mid) 100%)}
.slider-arrow{position:absolute;top:284px;width:57px;height:57px}
.slider-arrow.prev{left:169px}
.slider-arrow.next{left:977px}
.slider-dots{position:absolute;left:580px;top:477px;display:flex;gap:5px}
.slider-dots i{width:10px;height:10px;border-radius:50%;background:var(--dot);border:1px solid #6d5646}
.intro{position:absolute;left:170px;top:518px;width:860px;text-align:center;font-size:19px;line-height:21.5px;color:var(--text-light)}
.footer-nav{position:absolute;left:0;top:674px;width:1200px;text-align:center;font-size:17px;color:var(--text-muted)}
.footer-nav a{color:var(--text-muted);text-decoration:none;margin:0 11px}
.social{position:absolute;left:550px;top:731px;display:flex;gap:8px}
.social span{width:22px;height:22px;border-radius:4px;background:#7b8a96;display:block}
</style>
</head>
<body>
<div class="page-top"></div>
<div class="band"></div>
<div class="accent-line"></div>

<header>
  <div class="info-bar">
    <span>
      <svg width="8" height="11" viewBox="0 0 8 11" aria-hidden="true"><path d="M4 0a4 4 0 0 0-4 4c0 3 4 7 4 7s4-4 4-7a4 4 0 0 0-4-4zm0 5.5a1.5 1.5 0 1 1 0-3 1.5 1.5 0 0 1 0 3z" fill="#b9a697"/></svg>
      118 HARBOR LANE, PORTSIDE, NY
    </span>
    <span>
      <svg width="7" height="11" viewBox="0 0 7 11" aria-hidden="true"><rect x="0.5" y="0.5" width="6" height="10" rx="1" fill="none" stroke="#b9a697"/><rect x="2.5" y="8.5" width="2" height="1" fill="#b9a697"/></svg>
      (212) 555 - 0147
    </span>
  </div>
  <h1 class="site-name">Kefalos Tavern</h1>
  <nav class="main-nav">
    <div class="rule"></div>
    <ul>
      <li><a href="#">About Us</a></li>
      <li><a href="#">Menus</a></li>
      <li><a href="#">Gallery</a></li>
      <li><a href="#">Events</a></li>
      <li><a href="#">Blog</a></li>
      <li><a href="#">Contact</a></li>
    </ul>
    <div class="rule"></div>
  </nav>
</header>

<main>
  <div class="slider">
    <div class="slide-photo" role="img" aria-label="Featured dish photo: fresh salad with grilled chicken on a white plate"></div>
  </div>
  <svg class="slider-arrow prev" viewBox="0 0 57 57" aria-label="Previous slide"><circle cx="28.5" cy="28.5" r="28" fill="#8a8a8a" fill-opacity=".9"/><path d="M33 16 L21 28.5 L33 41" fill="none" stroke="#fff" stroke-width="2"/></svg>
  <svg class="slider-arrow next" viewBox="0 0 57 57" aria-label="Next slide"><circle cx="28.5" cy="28.5" r="28" fill="#8a8a8a" fill-opacity=".9"/><path d="M24 16 L36 28.5 L24 41" fill="none" stroke="#fff" stroke-width="2"/></svg>
  <div class="slider-dots"><i></i><i></i><i></i></div>

  <p class="intro">Lorem ipsum dolor sit amet, consectetur adipiscing elit. Fusce sem diam, venenatis sed lectus ac, porttitor accumsan sem. Sed cursus facilisis ornare. Fusce commodo, dui efficitur viverra dignissim, sapien velit dapibus massa, vel sollicitudin ante justo et ligula. Morbi fermentum sit amet lacus eu mattis. Suspendisse feugiat auctor commodo. Lorem ipsum dolor sit amet, consectetur adipiscing.</p>
</main>

<footer>
  <nav class="footer-nav">
    <a href="#">Home</a>|<a href="#">About</a>|<a href="#">Menus</a>|<a href="#">Gallery</a>|<a href="#">Events</a>|<a href="#">Blog</a>|<a href="#">Contact</a>
  </nav>
  <div class="social">
    <span role="img" aria-label="Social link"></span>
    <span role="img" aria-label="Social link"></span>
    <span role="img" aria-label="Social link"></span>
    <span role="img" aria-label="Social link"></span>
    <span role="img" aria-label="Social link"></span>
    <span role="img" aria-label="Social link"></span>
  </div>
</footer>
</body>
</html>
```